CrestHornSupply.com

I need a new webdesign for a company in the San Jose/SF Bay area that showcases the financial benefits of buying used band instruments for junior high students.This would be opposed to the current and costly option of renting cheap quality instruments from the 2 or 3 local music stores that charge a monthly fee that over the years charges the buyer 3 or 4x over..
Instruments: focus in on Alto Sax, Trumpet, Flute, Clarinet, Trombone, Tenor Sax, Baritone
Target middle schools are Willowmere Middle School and Harlan Middle School in San Jose, CA. Both have award winning band programs.
Files attached may or may not be important.
Tabs Needed and funtional
Contact
Shopping Cart
Select Instrument
Checkout
Add to Cart, etc.
Instuments
quantity, etc.
trade in your instrument/sell your instrument
ability to add or take away new instruments for sale. including pictures
Additional questions or info, feel free to ask
Updates
Hi Designers,
Project Deadline Extended
Reason: In the next week you will be receiving specific content that will be required to be had on the website.
New desigins are still welcome. Please continue to contact me if you have questions about your individual designs.
Thanks!
Crest Horn

```html
<!DOCTYPE html>
<html lang="en">
<head>
<meta charset="utf-8">
<title>Crest Horn — Band Instruments</title>
<link href="https://fonts.googleapis.com/css2?family=Oswald:wght@400;500;700&family=Open+Sans:wght@400;600&display=swap" rel="stylesheet">
<style>
:root{
  --red:#d0111a;
  --red-dark:#a80d14;
  --ink:#222;
  --text:#555;
  --muted:#999;
  --line:#e2e2e2;
  --page:#f1f1f1;
  --panel:#fff;
  --topbar:#141414;
  --footer:#111;
  --footer-box:#1c1c1c;
  --green:#5fb13a;
  --tab:#e3e3e3;
}
*{box-sizing:border-box;margin:0;padding:0}
html,body{width:1200px;height:2732px;overflow:hidden}
body{position:relative;background:var(--page);font-family:"Open Sans",Arial,sans-serif;color:var(--text);font-size:13px}
.abs{position:absolute}

/* top bar */
.topbar{left:0;top:0;width:1200px;height:38px;background:var(--topbar);color:#ddd;font-family:"Oswald",sans-serif;font-size:12px}
.topbar .links{left:84px;top:0;height:38px;display:flex;gap:30px;align-items:center;text-transform:uppercase}
.topbar .links span{display:flex;gap:7px;align-items:center}
.topbar .flag{left:366px;top:0;width:34px;height:50px;background:var(--red);clip-path:polygon(0 0,100% 0,100% 100%,50% 80%,0 100%)}
.topbar .welcome{left:786px;top:0;height:38px;line-height:38px;font-family:"Open Sans",sans-serif;font-size:11px;color:#aaa}
.topbar .welcome b{color:#fff;font-weight:600}
.topbar .cart{left:1016px;top:0;width:112px;height:38px;background:var(--green);color:#fff;line-height:38px;text-align:center;font-size:12px}

/* header */
.logo{left:72px;top:54px;font-family:"Oswald",sans-serif;font-weight:700;font-size:52px;line-height:70px;color:var(--red);text-transform:uppercase;letter-spacing:1px}
.search{left:718px;top:72px;width:244px;height:40px;border:3px solid #e4e4e4;border-radius:22px;background:#fff;padding-left:14px;line-height:34px;font-size:12px;color:#555}
.social{left:976px;top:80px;display:flex;gap:10px}
.social i{display:block;width:22px;height:22px;background:#c8c8c8;border-radius:3px}

/* nav */
.nav{left:66px;top:143px;width:1060px;height:50px;background:var(--red);color:#fff;font-family:"Oswald",sans-serif;font-size:15px;text-transform:uppercase}
.nav .home{left:0;top:0;width:50px;height:50px;background:var(--red-dark);display:flex;align-items:center;justify-content:center}
.nav ul{left:68px;top:0;height:50px;display:flex;gap:22px;list-style:none;align-items:center}
.nav .other{right:20px;top:0;height:50px;display:flex;align-items:center;gap:20px}

/* hero */
.hero{left:66px;top:206px;width:1060px;height:388px;background:linear-gradient(90deg,#3b2a20 0%,#6e5440 35%,#a58a70 55%,#5a4434 80%,#2c1f17 100%)}
.hero .title{left:0;width:1060px;top:148px;text-align:center;color:#fff;font-family:"Oswald",sans-serif;font-size:38px;letter-spacing:1px;text-transform:uppercase}
.hero .sub{left:0;width:1060px;top:206px;text-align:center;color:#fff;font-size:17px;letter-spacing:1px}
.hero .arrow{width:54px;height:54px;border-radius:50%;display:flex;align-items:center;justify-content:center}
.hero .dots{left:500px;top:352px;display:flex;gap:8px}
.hero .dots i{width:12px;height:12px;border:1px solid #fff;display:block}
.side-tab{width:32px;height:40px;background:#8a8a8a}

/* content panel */
.panel{left:74px;top:608px;width:1054px;height:1786px;background:var(--panel);border:1px solid var(--line)}
.section-title{font-family:"Oswald",sans-serif;font-size:17px;text-transform:uppercase;color:var(--ink);padding-bottom:6px;border-bottom:1px solid var(--line)}
.section-title::after{content:"";display:block;width:64px;height:2px;background:var(--red);margin-top:6px;margin-bottom:-7px}
.pager{display:flex;gap:6px}
.pager i{width:22px;height:22px;border:1px solid #ddd;border-radius:50%;display:flex;align-items:center;justify-content:center;font-style:normal;font-size:12px;color:#777}

.gallery-item{top:688px;width:228px;height:252px}

.tabs{left:96px;top:966px;display:flex;gap:6px}
.tabs div{width:248px;height:42px;background:var(--tab);font-family:"Oswald",sans-serif;font-size:14px;text-transform:uppercase;text-align:center;line-height:42px;color:#333}
.tabs .active{background:var(--red);color:#fff}

.product{width:190px}
.product .photo{height:172px;background:radial-gradient(circle at 50% 50%,#d9b15a 0%,#efe3c6 45%,#fff 72%);border-bottom:1px solid var(--line)}
.product .name{font-family:"Oswald",sans-serif;font-size:12px;text-transform:uppercase;color:#333;margin-top:14px;white-space:nowrap}
.product .price{font-family:"Oswald",sans-serif;font-size:14px;color:#333;margin-top:2px}
.product .price s{color:var(--muted);margin-right:6px}
.product .price .now{color:var(--red)}
.sale{width:40px;height:40px;border-radius:50%;background:var(--red);color:#fff;border:3px solid #fff;box-shadow:0 0 0 1px #ddd;font-family:"Oswald",sans-serif;font-size:11px;display:flex;align-items:center;justify-content:center}

.promo{top:1578px;width:354px;height:174px;color:#fff}
.promo h3{font-family:"Oswald",sans-serif;font-weight:500;font-size:19px;text-transform:uppercase;margin:20px 0 6px 50px}
.promo p{font-family:Georgia,serif;font-style:italic;font-size:12px;line-height:15px;margin-left:50px;width:230px;opacity:.9}
.promo .more{left:228px;top:126px;border:1px solid #fff;padding:4px 10px;font-family:"Oswald",sans-serif;font-size:11px;text-transform:uppercase}

.welcome-text p{font-size:12px;line-height:19px;color:#555}

.article{top:2003px;width:222px}
.article .photo{height:140px}
.article h4{font-family:"Oswald",sans-serif;font-weight:400;font-size:21px;text-transform:uppercase;color:var(--ink);margin-top:18px}
.article .date{font-size:10px;color:var(--muted)}
.article p{font-size:12px;line-height:17px;margin-top:8px;color:#555}

.sidebar{left:918px;width:190px}
.btn-red{background:var(--red);color:#fff;font-family:"Oswald",sans-serif;font-size:17px;text-transform:uppercase;text-align:center;line-height:48px;height:48px}
.field{height:32px;border:1px solid #ccc;font-size:11px;color:#aaa;padding-left:8px;line-height:30px;margin-bottom:12px}
.btn-green{background:var(--green);color:#fff;font-family:"Oswald",sans-serif;font-size:16px;text-transform:uppercase;text-align:center;line-height:46px;height:46px}

/* footer */
.footer{left:0;top:2396px;width:1200px;height:336px;background:var(--footer)}
.footer .edge{left:0;top:-10px;width:1200px;height:20px}
.fcol{top:52px;width:186px;height:182px;background:var(--footer-box);padding:16px 14px;color:#ddd}
.fcol h5{font-family:"Oswald",sans-serif;font-weight:400;font-size:14px;text-transform:uppercase;color:#fff;margin-bottom:16px}
.fcol li{list-style:none;font-family:"Oswald",sans-serif;font-size:12px;margin-bottom:11px;display:flex;gap:6px;align-items:center}
.footer .copy{left:0;width:1200px;top:296px;text-align:center;font-size:10px;color:#aaa}
</style>
</head>
<body>

<div class="abs topbar">
  <div class="abs links">
    <span><svg width="14" height="12" viewBox="0 0 14 12"><path d="M1 1h9v6H5l-3 3V7H1z" fill="#ddd"/></svg>Blogpage</span>
    <span><svg width="15" height="12" viewBox="0 0 15 12"><path d="M0 1h3l2 7h8l2-6H4" fill="none" stroke="#ddd" stroke-width="1.6"/><circle cx="6" cy="10.5" r="1.3" fill="#ddd"/><circle cx="12" cy="10.5" r="1.3" fill="#ddd"/></svg>Shop</span>
    <span><svg width="12" height="12" viewBox="0 0 12 12"><path d="M2 1l2 0 1 3-1.5 1a7 7 0 0 0 3.5 3.5L8 7l3 1v2c0 1-1 1-1 1A10 10 0 0 1 1 2s0-1 1-1z" fill="#ddd"/></svg>Contact</span>
  </div>
  <div class="abs flag"><svg width="34" height="40" viewBox="0 0 34 40"><circle cx="17" cy="12" r="2.2" fill="#fff"/><rect x="15" y="17" width="4" height="14" fill="#fff"/></svg></div>
  <div class="abs welcome">Welcome Visitor, you can <b>Login/Register</b></div>
  <div class="abs cart">1 ITEM(S) &nbsp;$0 &nbsp;▣</div>
</div>

<div class="abs logo">Crest Horn</div>
<div class="abs search">Search
  <svg class="abs" style="right:14px;top:11px" width="13" height="13" viewBox="0 0 13 13"><circle cx="5.5" cy="5.5" r="4" fill="none" stroke="#ccc" stroke-width="1.6"/><path d="M8.5 8.5l3.5 3.5" stroke="#ccc" stroke-width="1.6"/></svg>
</div>
<div class="abs social"><i></i><i></i><i></i><i></i><i></i></div>

<nav class="abs nav">
  <div class="abs home"><svg width="20" height="18" viewBox="0 0 20 18"><path d="M10 1L1 9h3v8h5v-5h2v5h5V9h3z" fill="#fff"/></svg></div>
  <ul class="abs"><li>About Us</li><li>Alto Sax</li><li>Trumpet</li><li>Flute</li><li>Clarinet</li><li>Trombone</li><li>Tenor Sax</li><li>Baritone</li></ul>
  <div class="abs other">Other Instruments <svg width="18" height="10" viewBox="0 0 18 10"><path d="M1 1l8 7 8-7" fill="none" stroke="#fff" stroke-width="2"/></svg></div>
</nav>

<div class="abs side-tab" style="left:0;top:222px"></div>
<div class="abs side-tab" style="left:0;top:276px"></div>
<div class="abs side-tab" style="left:1168px;top:222px"></div>

<section class="abs hero" role="img" aria-label="Photo of a saxophone player sitting by a window overlooking a city skyline">
  <div class="abs title">Better Quality at Lower Prices</div>
  <div class="abs sub">Be the new owner of the instrument you’ve been looking for</div>
  <div class="abs arrow" style="left:6px;top:164px;background:rgba(255,255,255,.85)"><svg width="16" height="18" viewBox="0 0 16 18"><path d="M12 2L4 9l8 7" fill="none" stroke="#333" stroke-width="3"/></svg></div>
  <div class="abs arrow" style="left:1000px;top:164px;background:var(--red);border:3px solid #fff"><svg width="16" height="18" viewBox="0 0 16 18"><path d="M4 2l8 7-8 7" fill="none" stroke="#fff" stroke-width="3"/></svg></div>
  <div class="abs arrow" style="left:1000px;top:316px;background:rgba(255,255,255,.85)"><svg width="18" height="14" viewBox="0 0 18 14"><path d="M2 3l7 7 7-7" fill="none" stroke="#333" stroke-width="3"/></svg></div>
  <div class="abs dots"><i style="background:var(--red)"></i><i></i><i></i></div>
</section>

<main class="abs panel"></main>

<div class="abs section-title" style="left:92px;top:638px;width:1018px">Gallery</div>
<div class="abs pager" style="left:1056px;top:636px"><i>‹</i><i>›</i></div>
<div class="abs gallery-item" style="left:106px;background:linear-gradient(160deg,#7a6a58,#b8a68e 60%,#5a4a3a)" role="img" aria-label="Photo of a cellist playing outdoors"></div>
<div class="abs gallery-item" style="left:360px;background:linear-gradient(180deg,#8c7a5a,#d8cfc0 45%,#6a7a3e)" role="img" aria-label="Photo of a marching band on a field"></div>
<div class="abs gallery-item" style="left:614px;background:linear-gradient(180deg,#b7b0b8,#f2f2f4 45%,#5a4a86)" role="img" aria-label="Photo of marching band members in white plumed hats"></div>
<div class="abs gallery-item" style="left:866px;background:linear-gradient(120deg,#d0b37a,#8a6a40 50%,#2a2520)" role="img" aria-label="Photo of a pianist playing by a window"></div>

<div class="abs tabs"><div class="active">Recently Added</div><div>Featured Products</div><div>Special Offers</div><div>Signature Series</div></div>

<div class="abs product" style="left:98px;top:1040px"><div class="photo" style="background:radial-gradient(circle,#333 0%,#c9c9c9 40%,#fff 70%)" role="img" aria-label="Clarinet"></div><div class="name">Arden AC110 Clarinet</div><div class="price"><s>$120.00</s><span class="now">$100.00</span></div></div>
<div class="abs product" style="left:300px;top:1040px"><div class="photo" style="background:radial-gradient(circle,#8a3a14 0%,#e0bfa8 40%,#fff 70%)" role="img" aria-label="Violin"></div><div class="name">Kestrel Model KV7 Violin</div><div class="price">$800.00</div></div>
<div class="abs product" style="left:502px;top:1040px"><div class="photo" role="img" aria-label="French horn"></div><div class="name">Hollis Single French Horn</div><div class="price">$120.00</div></div>
<div class="abs product" style="left:704px;top:1040px"><div class="photo" role="img" aria-label="Tenor saxophone"></div><div class="name">Vintage Marlow Tenor Sax</div><div class="price"><s>$300.00</s><span class="now">$275.00</span></div></div>
<div class="abs product" style="left:906px;top:1040px"><div class="photo" style="background:radial-gradient(circle,#1a1a1a 0%,#c4c4c4 40%,#fff 70%)" role="img" aria-label="Electric guitar"></div><div class="name">Garnet Royal Lucia Guitar</div><div class="price">$2399.00</div></div>
<div class="abs sale" style="left:102px;top:1046px">SALE</div>
<div class="abs sale" style="left:708px;top:1046px">SALE</div>

<div class="abs product" style="left:98px;top:1296px"><div class="photo" role="img" aria-label="Trombone"></div><div class="name">Baxter Trombone</div><div class="price">$170.00</div></div>
<div class="abs product" style="left:300px;top:1296px"><div class="photo" style="background:radial-gradient(circle,#2a2a2a 0%,#d0c8c0 40%,#fff 70%)" role="img" aria-label="Electric bass guitar"></div><div class="name">Fenwick American Std Bass</div><div class="price"><s>$1800.00</s><span class="now">$1690.00</span></div></div>
<div class="abs product" style="left:502px;top:1296px"><div class="photo" role="img" aria-label="Trumpet"></div><div class="name">Kestrel KT410 Trumpet</div><div class="price">$125.00</div></div>
<div class="abs product" style="left:704px;top:1296px"><div class="photo" style="background:radial-gradient(circle,#9a9a9a 0%,#e8e8e8 40%,#fff 70%)" role="img" aria-label="Flute"></div><div class="name">Glenhardt GF2 Flute</div><div class="price">$100.00</div></div>
<div class="abs product" style="left:906px;top:1296px"><div class="photo" role="img" aria-label="Baritone horn"></div><div class="name">B Flat Baritone 3 Valve</div><div class="price">$235.50</div></div>
<div class="abs sale" style="left:304px;top:1302px">SALE</div>

<div class="abs promo" style="left:100px;background:linear-gradient(120deg,#8a0a10,#d0111a 60%,#6a0a0c)" role="img" aria-label="Banner with guitar strings close-up">
  <h3>Make a gift to your loved ones</h3>
  <p>Vel illum dolore 25% eu feugiat nulla facilisis at vero eros et accumsan et iusto odio.</p>
  <div class="abs more">Learn More</div>
</div>
<div class="abs promo" style="left:492px;background:linear-gradient(120deg,#3a2412,#9a6a30 55%,#4a2e16)" role="img" aria-label="Banner with brass instrument close-up">
  <h3>Better Quality at Lower Prices</h3>
  <p>Vel illum dolore eu feugiat nulla facilisis at vero eros et accumsan et iusto odio.</p>
  <div class="abs more">Learn More</div>
</div>

<div class="abs welcome-text" style="left:92px;top:1796px;width:780px">
  <div class="section-title" style="border:none;padding:0">Welcome to Crest Horn</div>
  <p style="margin-top:16px">Lorem ipsum dolor sit amet, consectetuer adipiscing elit, sed diam nonummy nibh euismod tincidunt ut laoreet dolore magna aliquam erat volutpat. Ut wisi enim ad minim veniam, quis nostrud exerci tation ullamcorper suscipit lobortis nisl ut aliquip ex ea commodo consequat. Duis autem vel eum iriure dolor in hendrerit in vulputate velit esse molestie consequat, vel illum dolore eu feugiat nulla facilisis at vero eros et accumsan et iusto odio dignissim qui blandit praesent luptatum zzril delenit augue duis dolore te feugait nulla facilisi.</p>
</div>

<div class="abs section-title" style="left:92px;top:1944px;width:780px">Recent Articles</div>
<div class="abs article" style="left:98px"><div class="photo" style="background:linear-gradient(130deg,#3a1e10,#c07a30 55%,#5a2a14)" role="img" aria-label="Photo of an orchestra cellist performing"></div><h4>Mirum est notare</h4><div class="date">Mar 31, 2014</div><p>Lorem ipsum dolor sit amet, consectetuer adipiscing elit, sed diam nonummy nibh euismod tincidunt ut laoreet dolore magna aliquam erat volutpat. Ut wisi enim ad minim veniam.</p></div>
<div class="abs article" style="left:346px"><div class="photo" style="background:linear-gradient(180deg,#7a2a2a,#e8e0e0 40%,#b01818)" role="img" aria-label="Photo of marching band in red uniforms"></div><h4>Typi non habent</h4><div class="date">Mar 30, 2014</div><p>Lorem ipsum dolor sit amet, consectetuer adipiscing elit, sed diam nonummy nibh euismod tincidunt ut laoreet dolore magna aliquam erat volutpat. Ut wisi enim ad minim veniam.</p></div>
<div class="abs article" style="left:594px"><div class="photo" style="background:linear-gradient(180deg,#6a8a5a,#c03020 55%,#3a4a2a)" role="img" aria-label="Photo of a parade band marching outdoors"></div><h4>Vel illum dolore</h4><div class="date">Mar 29, 2014</div><p>Lorem ipsum dolor sit amet, consectetuer adipiscing elit, sed diam nonummy nibh euismod tincidunt ut laoreet dolore magna aliquam erat volutpat. Ut wisi enim ad minim veniam.</p></div>

<div class="abs sidebar" style="top:1550px">
  <div class="section-title">Deal of the Day</div>
</div>
<div class="abs pager" style="left:1056px;top:1558px"><i>‹</i><i>›</i></div>
<div class="abs product" style="left:918px;top:1604px"><div class="photo" role="img" aria-label="Alto saxophone"></div><div class="name">Yanase AS640 Alto Sax</div><div class="price"><s>$450.00</s><span class="now">$425.50</span></div></div>
<div class="abs sale" style="left:934px;top:1610px">SALE</div>
<div class="abs sidebar btn-red" style="top:1882px">Submit an Ad. It’s Free.</div>
<div class="abs sidebar" style="top:1980px">
  <div class="section-title">Feedback</div>
  <div style="margin-top:22px">
    <div class="field">Email</div>
    <div class="field">First Name</div>
    <div class="field">Last Name</div>
    <div class="field" style="height:100px">Message</div>
  </div>
  <div class="btn-green" style="margin-top:8px">Submit</div>
</div>

<footer class="abs footer">
  <svg class="abs edge" viewBox="0 0 1200 20" preserveAspectRatio="none"><path d="M0 10 L40 6 L90 12 L150 5 L220 11 L300 7 L360 12 L430 6 L510 10 L580 5 L660 12 L740 7 L820 11 L900 5 L980 10 L1060 6 L1130 12 L1200 8 V20 H0z" fill="#111"/></svg>
  <div class="abs fcol" style="left:72px"><h5>Information</h5><ul><li>✔ About Us</li><li>✔ Delivery &amp; Returns</li><li>✔ Submit an Ad</li><li>✔ Sale and Promotion</li></ul></div>
  <div class="abs fcol" style="left:270px"><h5>My Account</h5><ul><li>✔ My Account</li><li>✔ Cart</li><li>✔ Shop</li><li>✔ Checkout</li></ul></div>
  <div class="abs fcol" style="left:468px"><h5>Top Products</h5><ul><li>✔ Alto Saxophone</li><li>✔ Trumpet</li><li>✔ Flute</li><li>✔ Clarinet</li></ul></div>
  <div class="abs fcol" style="left:666px"><h5>Top Products</h5><ul><li>✔ Trombone</li><li>✔ Tenor Saxophone</li><li>✔ Baritone</li></ul></div>
  <div class="abs fcol" style="left:864px;width:200px"><h5>Contact Us</h5><ul>
    <li><svg width="11" height="11" viewBox="0 0 12 12"><path d="M2 1l2 0 1 3-1.5 1a7 7 0 0 0 3.5 3.5L8 7l3 1v2c0 1-1 1-1 1A10 10 0 0 1 1 2s0-1 1-1z" fill="#ccc"/></svg>+1 408 555 0146</li>
    <li><svg width="11" height="11" viewBox="0 0 12 12"><rect x="3" y="0.5" width="6" height="11" rx="1" fill="none" stroke="#ccc"/></svg>+1 408 555 0156</li>
    <li><svg width="12" height="10" viewBox="0 0 12 10"><rect x="0.5" y="0.5" width="11" height="9" fill="none" stroke="#ccc"/><path d="M1 1l5 4 5-4" fill="none" stroke="#ccc"/></svg>info@cresthorn.com</li>
  </ul></div>
  <div class="abs copy">Copyright © 2014 Crest Horn. All rights reserved.</div>
</footer>

</body>
</html>
```